Accountants new website

I have a logo and stationery style in design (nearly finished) but now need a wordpress template/skin to match my company livery.

the chosen logo and stationery can be found at pixelforge project "linked to design #14688513. KQ Studios 2016, World Class. This will be finalised very soon and all images available for use.

Target Market(s)

businesses, financial planning clients (young and old)

Industry/Entity Type

Financial Planning

Font styles to use
Sans Serif

Colors
f37122

Requirements
Must have
• happy business and lifestyle images
• more logos
• - TV nrl
• LMB
• GUD
• HOTW
• Levy Guild
• Financial PLanning Group - Marvola
• OTP
• ZUK
• Plumo
• Professional cover of excellence
Nice to have
• Harbour Gain (Logo & Trading Name)
• Harbour Gain Consulting Pty Limited (company name)
• ACN 728401956
• Accountants & Business Advisors
• Telephone 1300 486 507
• Fax 612 4598 3307
• Postal address - PO Box 5814, Erina, NSW, 2250
• Mobile 0417 538 064
• Business Address
• Suite 3.07, 9 Tamsin Crescent, Erina NSW 2250
• mail@ harbourgain.com.au
• Website harbourgain.com.au
• BUSINESS CARD (2 sided)
• Neil Fairhurst FCA
• Managing Director
• Mobile 0417 53 80 64
• Email: neil.f@harbourgain.com.au
• Logo - Harbour Gain, Chartered Accountant (Small round)
• List of services;
• Tax and Accounting
• Business Development
• Superannuation and Financial Services
• LOGOS
• 1. Ledger Auditors
• 2. Plumo
• 3. Professional liability logo
• 4. Revenue Guild
• 5. LMB
• 6. HOTW - superannuation
• 7 GUD - fin planning
Should not have
• must be scaleable so I can grow it over time
• must not be old style

```html
<!DOCTYPE html>
<html lang="en">
<head>
<meta charset="utf-8">
<title>Harbour Gain Consulting</title>
<link href="https://fonts.googleapis.com/css2?family=Open+Sans:wght@400;600;700&display=swap" rel="stylesheet">
<style>
:root{
  --orange:#f37122;
  --ink:#222;
  --body:#666;
  --muted:#888;
  --line:#d9d9d9;
  --white:#fff;
}
*{margin:0;padding:0;box-sizing:border-box}
html,body{width:742px;height:1200px;overflow:hidden;background:var(--white)}
body{position:relative;font-family:"Open Sans",Arial,sans-serif;color:var(--ink)}
.abs{position:absolute}

/* hero */
.hero{left:0;top:0;width:742px;height:345px;overflow:hidden}
.hero-photo{position:absolute;inset:0;background:
  linear-gradient(180deg,#2c3242 0%,#4b4f5b 22%,#b78a55 40%,#6d6a6c 50%,#38465e 62%,#2d3a52 100%)}
.hero-curve{position:absolute;left:0;top:0}
.brand{left:60px;top:29px}
.brand-name{color:var(--white);font-size:15px;font-weight:600;letter-spacing:0}
.contact-top{top:15px;right:60px;display:flex;gap:18px;color:var(--white);font-size:11px;font-weight:600}
.contact-top span{display:flex;align-items:center;gap:7px}
.nav{top:41px;right:60px;display:flex;gap:22px;font-size:9.5px;font-weight:600;color:var(--white);align-items:center}
.nav .active{color:var(--orange)}
.hero-title{top:120px;width:742px;text-align:center;color:var(--white);font-size:27px;font-weight:600;text-shadow:0 1px 3px rgba(0,0,0,.4)}
.hero-sub{top:158px;width:742px;text-align:center;color:var(--white);font-size:16px}
.hero-btn{left:313px;top:194px;width:116px;height:26px;border:1px solid var(--white);border-radius:13px;color:var(--white);font-size:8.5px;font-weight:600;text-align:center;line-height:24px}
.dots{left:349px;top:286px;display:flex;gap:4px}
.dots i{width:8px;height:8px;border-radius:50%;border:1px solid var(--white)}
.dots i:first-child{background:var(--white)}

/* welcome */
.welcome-title{top:390px;width:742px;text-align:center;font-size:15px;font-weight:600}
.welcome-text{top:424px;left:120px;width:502px;text-align:center;font-size:7.5px;line-height:15.5px;color:var(--body)}

/* services */
.card{top:487px;width:195px;height:246px;border:1px solid #e2e2e2;box-shadow:0 1px 3px rgba(0,0,0,.08);background:var(--white)}
.card-photo{position:absolute;left:2px;top:2px;width:189px;height:118px}
.card-curve{position:absolute;left:0;top:80px}
.card-icon{position:absolute;left:77px;top:104px;width:40px;height:40px;border-radius:50%;background:var(--orange);border:3px solid var(--white);box-shadow:0 0 0 1px var(--orange);display:flex;align-items:center;justify-content:center}
.card-title{position:absolute;top:158px;width:100%;text-align:center;font-size:12px;font-weight:600}
.card-text{position:absolute;top:181px;left:14px;right:14px;text-align:center;font-size:7.3px;line-height:14.5px;color:var(--body)}
.card-btn{position:absolute;left:58px;bottom:-13px;width:78px;height:25px;border:1px solid #ddd;border-radius:13px;background:var(--white);color:var(--orange);font-size:7.5px;font-weight:700;text-align:center;line-height:23px}

.divider{left:60px;width:622px;height:1px;background:var(--line)}

/* partners */
.partners-title{top:837px;width:742px;text-align:center;font-size:15px;font-weight:600}
.partner{top:878px;width:112px;height:57px;border:1px solid #cfcfcf;display:flex;align-items:center;justify-content:center;gap:7px;font-size:11px;font-weight:600;color:#333}
.partner i{width:16px;height:16px;background:#444}
.partner i.round{border-radius:50%}
.arrow{top:897px}

/* footer */
.footer-band{top:992px;left:0;width:742px;height:2px;background:var(--orange)}
.finfo{display:flex;align-items:center;gap:10px;font-size:7.8px;color:var(--body)}
.ficon{width:29px;height:29px;border-radius:50%;border:1px solid #ccc;display:flex;align-items:center;justify-content:center}
.flinks{top:1155px;left:61px;font-size:7.8px;color:var(--body);word-spacing:2px}
.copy{top:1174px;left:61px;font-size:7.3px;color:var(--body)}
.social{top:1155px;left:570px;display:flex;gap:5px}
.social i{width:19px;height:19px;border-radius:50%;border:1px solid var(--orange)}
</style>
</head>
<body>

<section class="abs hero">
  <div class="hero-photo" role="img" aria-label="Harbour city skyline at dusk with bridge and moored sailing boats"></div>
  <svg class="hero-curve" width="742" height="345" viewBox="0 0 742 345">
    <path d="M0 282 Q371 390 742 280 L742 345 L0 345 Z" fill="#fff"/>
    <path d="M0 282 Q371 390 742 280" fill="none" stroke="#f37122" stroke-width="3"/>
  </svg>
  <div class="abs brand"><span class="brand-name">Harbour Gain</span></div>
  <div class="abs contact-top">
    <span><svg width="11" height="11" viewBox="0 0 24 24"><path fill="#f37122" d="M6.6 10.8a15 15 0 006.6 6.6l2.2-2.2c.3-.3.7-.4 1-.2 1.1.4 2.3.6 3.6.6.6 0 1 .4 1 1V20c0 .6-.4 1-1 1A17 17 0 013 4c0-.6.4-1 1-1h3.5c.6 0 1 .4 1 1 0 1.3.2 2.5.6 3.6.1.3 0 .7-.2 1z"/></svg>1300 486 507</span>
    <span><svg width="12" height="9" viewBox="0 0 24 18"><rect width="24" height="18" rx="2" fill="#f37122"/><path d="M1 2l11 8 11-8" fill="none" stroke="#fff" stroke-width="2"/></svg>mail@harbourgain.com.au</span>
  </div>
  <nav class="abs nav">
    <span class="active">HOME</span><span>WHY HARBOUR</span><span>OUR SERVICES</span><span>PRICING</span><span>CONTACT</span>
    <svg width="9" height="9" viewBox="0 0 24 24"><circle cx="10" cy="10" r="7" fill="none" stroke="#fff" stroke-width="3"/><path d="M15 15l7 7" stroke="#fff" stroke-width="3"/></svg>
  </nav>
  <h1 class="abs hero-title">HARBOUR GAIN CONSULTING</h1>
  <p class="abs hero-sub">Accountants &amp; Business Advisors</p>
  <div class="abs hero-btn">GET MORE INFO &gt;&gt;</div>
  <div class="abs dots"><i></i><i></i><i></i><i></i></div>
</section>

<h2 class="abs welcome-title">WELCOME TO HARBOUR GAIN CONSULTING</h2>
<p class="abs welcome-text">At vero eos et accusamus et iusto odio dignissimos ducimus qui blanditiis praesentium voluptatum deleniti atque corrupti quos dolores et quas molestias excepturi sint occaecati cupiditate non provident, similique sunt in culpa qui officia deserunt mollitia</p>

<article class="abs card" style="left:60px">
  <div class="card-photo" role="img" aria-label="Hands using a calculator over printed accounts" style="background:linear-gradient(135deg,#8a96a6,#d9dde2 55%,#b9bcc0)"></div>
  <svg class="card-curve" width="193" height="45" viewBox="0 0 193 45"><path d="M0 22 Q96 64 193 22 L193 45 L0 45Z" fill="#fff"/><path d="M0 22 Q96 64 193 22" fill="none" stroke="#f37122" stroke-width="2"/></svg>
  <div class="card-icon"><svg width="16" height="16" viewBox="0 0 16 16"><rect x="1" y="1" width="14" height="14" fill="none" stroke="#fff" stroke-width="1.5"/><path d="M1 5h14M5 5v10M8 5v10M11 5v10M1 8h14M1 11h14" stroke="#fff" stroke-width="1"/></svg></div>
  <h3 class="card-title">Tax and Accounting</h3>
  <p class="card-text">Nam libero tempore, cum soluta nobis est eligendi optio cumque nihil impedit quo minus id quod maxime placeat facerossi</p>
  <div class="card-btn">READ MORE &gt;&gt;</div>
</article>

<article class="abs card" style="left:274px">
  <div class="card-photo" role="img" aria-label="Hand placing a wooden block on a stacked block tower" style="background:linear-gradient(135deg,#3e4a5e,#a59a8c 55%,#6b6d72)"></div>
  <svg class="card-curve" width="193" height="45" viewBox="0 0 193 45"><path d="M0 22 Q96 64 193 22 L193 45 L0 45Z" fill="#fff"/><path d="M0 22 Q96 64 193 22" fill="none" stroke="#f37122" stroke-width="2"/></svg>
  <div class="card-icon"><svg width="18" height="16" viewBox="0 0 18 16"><circle cx="7" cy="9" r="4.5" fill="none" stroke="#fff" stroke-width="2.5" stroke-dasharray="2 1.5"/><circle cx="14" cy="4" r="2.8" fill="none" stroke="#fff" stroke-width="2" stroke-dasharray="1.5 1.2"/></svg></div>
  <h3 class="card-title">Business Development</h3>
  <p class="card-text">Nam libero tempore, cum soluta nobis est eligendi optio cumque nihil impedit quo minus id quod maxime placeat facerossi</p>
  <div class="card-btn">READ MORE &gt;&gt;</div>
</article>

<article class="abs card" style="left:487px">
  <div class="card-photo" role="img" aria-label="Hands reviewing charts on a tablet at a bright desk" style="background:linear-gradient(135deg,#e8ecef,#cfd8de 50%,#f2f2f0)"></div>
  <svg class="card-curve" width="193" height="45" viewBox="0 0 193 45"><path d="M0 22 Q96 64 193 22 L193 45 L0 45Z" fill="#fff"/><path d="M0 22 Q96 64 193 22" fill="none" stroke="#f37122" stroke-width="2"/></svg>
  <div class="card-icon"><svg width="18" height="12" viewBox="0 0 18 12"><rect x="1" y="1" width="16" height="10" fill="none" stroke="#fff" stroke-width="1.8"/><circle cx="9" cy="6" r="2.3" fill="#fff"/></svg></div>
  <h3 class="card-title">Superannuation &amp; Financial</h3>
  <p class="card-text">Nam libero tempore, cum soluta nobis est eligendi optio cumque nihil impedit quo minus id quod maxime placeat facerossi</p>
  <div class="card-btn">READ MORE &gt;&gt;</div>
</article>

<div class="abs divider" style="top:795px"></div>

<h2 class="abs partners-title">OUT PARTNERS</h2>
<svg class="abs arrow" style="left:36px" width="12" height="18" viewBox="0 0 12 18"><path d="M10 1L2 9l8 8" fill="none" stroke="#aaa" stroke-width="1.5"/></svg>
<div class="abs partner" style="left:62px"><i></i>HOTW</div>
<div class="abs partner" style="left:189px"><i class="round"></i>GUD</div>
<div class="abs partner" style="left:316px"><i></i>LMB</div>
<div class="abs partner" style="left:443px"><i></i>Levy Guild</div>
<div class="abs partner" style="left:570px"><i class="round"></i>Plumo</div>
<svg class="abs arrow" style="left:694px" width="12" height="18" viewBox="0 0 12 18"><path d="M2 1l8 8-8 8" fill="none" stroke="#aaa" stroke-width="1.5"/></svg>

<div class="abs footer-band"></div>

<div class="abs finfo" style="left:97px;top:1035px"><span class="ficon"><svg width="10" height="13" viewBox="0 0 10 13"><path d="M5 12S1 7 1 4.5a4 4 0 018 0C9 7 5 12 5 12z" fill="#f37122"/><circle cx="5" cy="4.5" r="1.5" fill="#fff"/></svg></span>PO Box 5814, Erina, NSW, 2250</div>
<div class="abs finfo" style="left:97px;top:1077px"><span class="ficon"><svg width="10" height="13" viewBox="0 0 10 13"><path d="M5 12S1 7 1 4.5a4 4 0 018 0C9 7 5 12 5 12z" fill="#f37122"/><circle cx="5" cy="4.5" r="1.5" fill="#fff"/></svg></span>Suite 3.07, 9 Tamsin Crescent, Erina NSW 2250</div>
<div class="abs finfo" style="left:325px;top:1035px"><span class="ficon"><svg width="11" height="11" viewBox="0 0 24 24"><path fill="#f37122" d="M6.6 10.8a15 15 0 006.6 6.6l2.2-2.2c.3-.3.7-.4 1-.2 1.1.4 2.3.6 3.6.6.6 0 1 .4 1 1V20c0 .6-.4 1-1 1A17 17 0 013 4c0-.6.4-1 1-1h3.5c.6 0 1 .4 1 1 0 1.3.2 2.5.6 3.6.1.3 0 .7-.2 1z"/></svg></span>1300 486 507 &nbsp;|&nbsp; 0417 538 064</div>
<div class="abs finfo" style="left:325px;top:1077px"><span class="ficon"><svg width="12" height="12" viewBox="0 0 12 12"><rect x="1" y="4" width="10" height="7" fill="#f37122"/><rect x="3" y="1" width="6" height="4" fill="none" stroke="#f37122" stroke-width="1.2"/><path d="M3 7h6M3 9h6" stroke="#fff" stroke-width=".8"/></svg></span>612 4598 3307</div>
<div class="abs finfo" style="left:505px;top:1035px"><span class="ficon"><svg width="12" height="9" viewBox="0 0 24 18"><rect width="24" height="18" rx="2" fill="#f37122"/><path d="M1 2l11 8 11-8" fill="none" stroke="#fff" stroke-width="2"/></svg></span>mail@harbourgain.com.au</div>
<div class="abs finfo" style="left:505px;top:1077px"><span class="ficon"><svg width="13" height="10" viewBox="0 0 13 10"><rect x=".5" y=".5" width="12" height="9" rx="1" fill="none" stroke="#f37122"/><path d="M.5 3.5h12" stroke="#f37122" stroke-width="1.5"/></svg></span>ACN 728401956</div>

<div class="abs divider" style="top:1133px"></div>
<div class="abs flinks">Home &nbsp;| &nbsp;Why Harbour &nbsp;| &nbsp;Our Services &nbsp;| &nbsp;Pricing &nbsp;| &nbsp;Contact</div>
<div class="abs copy">Copyrights © 2017, Harbour Gain. All rights reserved.</div>
<div class="abs social"><i></i><i></i><i></i><i></i><i></i></div>

</body>
</html>
```